Need a Facebook image for childcare advertisement

We are after a design for Facebook advertisement for childcare and kindergarten centre enrolments for 2023.

I have attached a previous flyer that we have in pdf format. The new logo is also attached with this brief.

All other information is still current as per the attached flyer.

You can use same colours as per attached flyer. I will also attached some stock images that you can select to use for the design.

our website for your reference:

https://tolvenbrook.com.au

```html
<!DOCTYPE html>
<html lang="en">
<head>
<meta charset="UTF-8">
<title>Tolvenbrook Early Childhood Learning Centre</title>
<link rel="stylesheet" href="https://fonts.googleapis.com/css2?family=Fira+Sans:wght@400;700&family=Fira+Sans+Condensed:wght@400&display=swap">
<style>
  :root {
    --brand-red: #e8403d;
    --brand-red-soft: rgba(232, 64, 61, 0.55);
    --white: #ffffff;
    --photo-warm: #c98a6a;
    --photo-blue: #3d5a85;
    --photo-pink: #b2578e;
    --photo-floor: #c44a4f;
  }
  * { margin: 0; padding: 0; box-sizing: border-box; }
  html, body {
    width: 1200px;
    height: 675px;
    overflow: hidden;
    background: var(--white);
  }
  .ad {
    position: relative;
    width: 1200px;
    height: 675px;
    overflow: hidden;
    font-family: "Fira Sans", Arial, sans-serif;
    color: var(--white);
  }
  .hero-photo {
    position: absolute;
    inset: 0;
    background:
      radial-gradient(ellipse at 20% 40%, rgba(61, 90, 133, 0.85), transparent 45%),
      radial-gradient(ellipse at 85% 55%, rgba(178, 87, 142, 0.85), transparent 40%),
      radial-gradient(ellipse at 50% 35%, rgba(40, 50, 80, 0.7), transparent 35%),
      linear-gradient(180deg, #d9d2cc 0%, var(--photo-warm) 45%, var(--photo-floor) 100%);
  }
  .brand {
    position: absolute;
    top: 120px;
    left: 0;
    width: 1200px;
    text-align: center;
  }
  .brand-name {
    font-weight: 700;
    font-size: 60px;
    letter-spacing: 2px;
    line-height: 1;
    text-transform: uppercase;
  }
  .brand-tagline {
    margin-top: 30px;
    font-family: "Fira Sans Condensed", "Arial Narrow", sans-serif;
    font-weight: 400;
    font-size: 31px;
    letter-spacing: 0.5px;
    text-transform: uppercase;
  }
  .offer-panel {
    position: absolute;
    left: 0;
    bottom: 0;
    width: 1200px;
    height: 275px;
  }
  .offer-copy {
    position: absolute;
    left: 42px;
    top: 440px;
  }
  .offer-headline {
    font-weight: 700;
    font-size: 41px;
    line-height: 54px;
  }
  .offer-body {
    margin-top: 12px;
    font-weight: 400;
    font-size: 32px;
    line-height: 48px;
  }
</style>
</head>
<body>
  <main class="ad">
    <div class="hero-photo" role="img" aria-label="Smiling educator sitting on a red carpet with four young children playing together in a bright classroom"></div>

    <header class="brand">
      <div class="brand-name">Tolvenbrook</div>
      <div class="brand-tagline">Early Childhood Learning Centre</div>
    </header>

    <svg class="offer-panel" viewBox="0 400 1200 275" preserveAspectRatio="none" aria-hidden="true">
      <defs>
        <linearGradient id="panelFade" x1="0" y1="0" x2="1" y2="0">
          <stop offset="0" stop-color="#e8403d" stop-opacity="1"/>
          <stop offset="0.55" stop-color="#e8403d" stop-opacity="0.92"/>
          <stop offset="1" stop-color="#e8403d" stop-opacity="0.55"/>
        </linearGradient>
      </defs>
      <path d="M0,430 C180,405 460,398 600,455 C760,525 900,625 1200,610 L1200,675 L0,675 Z" fill="url(#panelFade)"/>
    </svg>

    <section class="offer-copy">
      <h1 class="offer-headline">Spark A Lifelong Love<br>Of Learning In Your Child</h1>
      <p class="offer-body">Encourage them to explore, play, discover, and just be themselves<br>in a safe, nurturing environment.</p>
    </section>
  </main>
</body>
</html>
```